Vastelo.com webside

I want to build a Vastelo.com retail website use on Shopify, reselling three main categories: Office Supplies, Packing Supplies, and Home Consumables. I also wish the webpage has the same functions as the Quorvi home page. The page is split into three different parts with the top being a sliding screen showcasing promotion products, below it being the three categories, and finally, a moving screen showing company missions.
Target Market(s)
U.S online
Industry/Entity Type
Office Supplies, packing Supplies and Home Consumables
Look and feel
Each slider illustrates characteristics of the customer's brand and the style your logo design should communicate.

```html
<!DOCTYPE html>
<html lang="en">
<head>
<meta charset="utf-8">
<title>Vastelo – Office, Packing &amp; Home Supplies</title>
<link href="https://fonts.googleapis.com/css2?family=Josefin+Sans:wght@400;500;600;700&display=swap" rel="stylesheet">
<style>
:root{
  --green:#17a07b;
  --teal-light:#5bd1bd;
  --ink:#111111;
  --muted:#444444;
  --card-bg:#eef0f2;
  --white:#ffffff;
  --black:#000000;
}
*{margin:0;padding:0;box-sizing:border-box}
html,body{width:1200px;height:4435px;overflow:hidden}
body{font-family:"Josefin Sans",sans-serif;color:var(--ink);background:var(--white);position:relative}
.abs{position:absolute}
a{color:inherit;text-decoration:none}

.social{display:flex;gap:14px;align-items:center}
.social span{width:12px;height:12px;border:2px solid currentColor;border-radius:3px}
.social span:nth-child(2n){border-radius:50%}

.topbar{top:0;left:0;width:1200px;height:48px;background:var(--green);color:var(--black)}
.topbar .promo{left:112px;top:17px;font-size:15px;font-weight:600}
.topbar .social{right:112px;top:18px;color:var(--white)}

.nav{top:48px;left:0;width:1200px;height:78px;background:var(--white)}
.logo{font-weight:700;font-size:30px;letter-spacing:1px}
.nav .logo{left:112px;top:24px}
.menu{display:flex;gap:42px;font-size:17px;font-weight:500}
.nav .menu{left:396px;top:31px}
.nav-icons{right:112px;top:26px;display:flex;gap:36px}

.hero{top:126px;left:0;width:1200px;height:563px;
  background:
    radial-gradient(ellipse 120px 70px at 610px 490px,#f4f4f3 0%,rgba(244,244,243,0) 100%),
    radial-gradient(ellipse 260px 160px at 920px 330px,#8e9093 0%,rgba(142,144,147,0) 100%),
    radial-gradient(ellipse 110px 150px at 1150px 250px,#6f8a55 0%,rgba(111,138,85,0) 100%),
    linear-gradient(180deg,#e9e6e1 0%,#d9d5cf 55%,#e6e6e6 75%,#d2d2d2 100%)}
.hero .kicker{left:112px;top:160px;font-size:26px;font-weight:600}
.hero h1{left:112px;top:204px;font-size:46px;font-weight:700;letter-spacing:1px}
.hero .sub{left:112px;top:270px;font-size:20px;font-weight:500}
.btn{background:var(--green);color:var(--black);font-size:15px;font-weight:600;display:flex;align-items:center;justify-content:center}
.hero .b1{left:112px;top:308px;width:126px;height:38px}
.hero .b2{left:258px;top:308px;width:104px;height:38px}

.section-title{font-size:30px;font-weight:600;letter-spacing:1px}
.section-sub{font-size:15px;color:var(--muted)}
.section-link{font-size:16px;font-weight:500}

.type-card{top:806px;height:272px;background:var(--card-bg)}
.save-card{background:var(--green);padding:76px 0 0 29px}
.save-card h3{font-size:18px;font-weight:700}
.save-card p{font-size:11px;line-height:17px;margin-top:10px;width:180px}
.outline-btn{border:2px solid var(--black);font-size:13px;display:inline-flex;align-items:center;justify-content:center}
.save-card .outline-btn{width:82px;height:34px;margin-top:12px}

.band{left:0;width:1200px;height:449px}
.band .panel{left:0;top:0;height:449px}
.band h2{font-size:34px;font-weight:600;letter-spacing:1px}
.band p{font-size:11px;line-height:17px;width:180px;margin-top:10px}
.band .outline-btn{height:34px;padding:0 14px;margin-top:16px}
.band .copy{left:112px;top:152px}

.product{background:var(--white);box-shadow:0 0 14px rgba(0,0,0,.08);padding:9px}
.product .pic{width:100%;background:var(--card-bg)}
.product .name{font-size:12px;margin-top:20px}
.product .price{font-size:11px;margin-top:10px}
.badge{position:absolute;top:25px;left:16px;background:var(--green);font-size:12px;padding:4px 10px}
.old{color:var(--ink);margin-left:6px;text-decoration:line-through}
.price .now{color:var(--green)}

.footer{top:3882px;left:0;width:1200px;height:487px;background:var(--black);color:var(--white)}
.footer h2{left:112px;top:68px;font-size:30px;font-weight:600;letter-spacing:1px}
.footer .lead{left:112px;top:118px;font-size:15px;font-weight:500}
.signup{left:658px;top:54px;display:flex}
.signup .field{width:289px;height:49px;border:1px solid var(--white);font-size:12px;font-weight:600;padding:18px 20px}
.signup .send{width:141px;height:49px;background:var(--white);color:var(--black);font-size:13px;font-weight:600;display:flex;align-items:center;justify-content:center}
.footer .rule{left:112px;top:177px;width:976px;height:1px;background:#666}
.footer .logo{left:112px;top:250px}
.footer .menu{right:112px;top:256px;gap:42px;font-size:18px}
.footer .detail{left:112px;top:313px;font-size:16px;font-weight:500}
.footer .follow{left:112px;top:356px;font-size:16px;font-weight:500}
.footer .social{left:108px;top:411px;gap:18px}
.copyright{top:4369px;left:0;width:1200px;height:66px;background:var(--green);font-size:11px;display:flex;align-items:center;justify-content:center}
</style>
</head>
<body>

<header class="abs topbar">
  <span class="abs promo">Limited Time Only</span>
  <div class="abs social" aria-label="Social links"><span></span><span></span><span></span><span></span></div>
</header>

<nav class="abs nav">
  <span class="abs logo">VASTELO</span>
  <div class="abs menu"><a>Home</a><a>About</a><a>Shop</a><a>Blog</a><a>Contact</a></div>
  <div class="abs nav-icons">
    <svg width="24" height="24" viewBox="0 0 24 24" fill="none" stroke="#111" stroke-width="2"><circle cx="10" cy="10" r="7"/><path d="M15 15l7 7"/></svg>
    <svg width="24" height="24" viewBox="0 0 24 24" fill="none" stroke="#111" stroke-width="2"><circle cx="12" cy="8" r="5"/><path d="M3 23c0-5 4-8 9-8s9 3 9 8"/></svg>
    <svg width="28" height="24" viewBox="0 0 28 24" fill="none" stroke="#111" stroke-width="2"><path d="M1 2h4l3 14h15l3-10H7"/><circle cx="10" cy="21" r="2"/><circle cx="21" cy="21" r="2"/></svg>
  </div>
</nav>

<section class="abs hero" role="img" aria-label="Bright office desk with a laptop, a white mug and a potted plant">
  <span class="abs kicker">SAVE UPTO 70%</span>
  <h1 class="abs">Welcome To Vastelo</h1>
  <p class="abs sub">Excepteur sint occaecat cupidatat non</p>
  <a class="abs btn b1">Shop Cascual</a>
  <a class="abs btn b2">Shop All</a>
</section>

<h2 class="abs section-title" style="left:112px;top:748px">Shop by type</h2>
<div class="abs type-card" style="left:112px;width:229px;background:radial-gradient(ellipse 70px 60px at 50% 50%,#b98d5a 0%,#c9a57a 50%,rgba(238,240,242,0) 100%),var(--card-bg)" role="img" aria-label="Cardboard box with packing tape"></div>
<div class="abs type-card" style="left:363px;width:228px;background:radial-gradient(ellipse 90px 40px at 50% 50%,#d98a4a 0%,#c06a8a 45%,rgba(238,240,242,0) 100%),var(--card-bg)" role="img" aria-label="Pens, pencils and paper clips"></div>
<div class="abs type-card" style="left:611px;width:229px;background:radial-gradient(ellipse 80px 60px at 50% 55%,#c79a66 0%,#7a6a9a 45%,rgba(238,240,242,0) 100%),var(--card-bg)" role="img" aria-label="Open box of office supplies"></div>
<div class="abs type-card save-card" style="left:859px;width:229px">
  <h3>Save 25%</h3>
  <p>Duis aute irure dolor in reprehenderit in voluptate velit esse cillum</p>
  <a class="outline-btn">Shop</a>
</div>

<section class="abs band" style="top:1154px">
  <div class="abs panel" style="width:486px;background:var(--green)"></div>
  <div class="abs" style="left:486px;top:0;width:714px;height:449px;background:radial-gradient(ellipse 220px 200px at 250px 260px,#c9995e 0%,rgba(201,153,94,0) 100%),radial-gradient(ellipse 180px 160px at 640px 80px,#f2c58a 0%,rgba(242,197,138,0) 100%),linear-gradient(110deg,#2e2118,#6b4b30 50%,#a9744a)" role="img" aria-label="Stacked cardboard boxes beside a laptop"></div>
  <div class="abs copy">
    <h2>Casual Quality</h2>
    <p>Duis aute irure dolor in reprehenderit in voluptate velit esse cillum</p>
    <a class="outline-btn">Office Supplies</a>
  </div>
</section>

<h2 class="abs section-title" style="left:112px;top:1653px">Our favorites</h2>
<p class="abs section-sub" style="left:112px;top:1698px">Excepteur sint occaecat cupidatat</p>
<a class="abs section-link" style="left:112px;top:1730px">View All Products</a>
<div class="abs" style="left:112px;top:1768px;width:499px;height:341px;background:radial-gradient(ellipse 200px 90px at 250px 300px,#c49c6c 0%,rgba(196,156,108,0) 100%),linear-gradient(180deg,#d8dad6 0%,#2f4a30 45%,#284328 70%,#b9926a 100%)" role="img" aria-label="Volunteers packing food into cardboard boxes"></div>
<div class="abs product" style="left:632px;top:1770px;width:238px;height:335px"><div class="pic" style="height:263px;background:radial-gradient(ellipse 80px 60px at 50% 55%,#e04c7a 0%,#4a6fd0 45%,#f2d04a 70%,rgba(238,240,242,0) 100%),var(--card-bg)" role="img" aria-label="Colourful desk organiser with stationery"></div><p class="name">Office Supplies</p><p class="price">$23.00</p></div>
<div class="abs product" style="left:890px;top:1770px;width:238px;height:335px"><div class="pic" style="height:263px;background:radial-gradient(ellipse 80px 50px at 50% 50%,#c9bfa8 0%,#ddd6c6 55%,rgba(238,240,242,0) 100%),var(--card-bg)" role="img" aria-label="Two rolls of clear packing tape"></div><p class="name">Packing Supplies</p><p class="price">$23.00</p></div>
<div class="abs product" style="left:1149px;top:1770px;width:238px;height:335px"><div class="pic" style="height:263px;background:radial-gradient(ellipse 80px 60px at 50% 55%,#e8a23a 0%,#5aa0d0 50%,rgba(238,240,242,0) 100%),var(--card-bg)" role="img" aria-label="Office stationery set"></div><p class="name">Office Supplies</p><p class="price">$23.00</p></div>

<section class="abs band" style="top:2183px">
  <div class="abs panel" style="width:487px;background:var(--teal-light)"></div>
  <div class="abs" style="left:487px;top:0;width:713px;height:449px;background:radial-gradient(ellipse 80px 200px at 300px 250px,#d79a7e 0%,rgba(215,154,126,0) 100%),radial-gradient(ellipse 160px 60px at 420px 330px,#a36a40 0%,rgba(163,106,64,0) 100%),linear-gradient(180deg,#6e4e36 0%,#7c6650 12%,#8fa8a6 30%,#9fb3b0 70%,#c5c8c2 100%)" role="img" aria-label="Woman setting a breakfast table in a kitchen"></div>
  <div class="abs copy">
    <h2>Home Consumables</h2>
    <p>Duis aute irure dolor in reprehenderit in voluptate velit esse cillum</p>
    <a class="outline-btn">Home Consumables</a>
  </div>
</section>

<h2 class="abs section-title" style="left:110px;top:2687px">Most popular</h2>
<p class="abs section-sub" style="left:110px;top:2732px">Excepteur sint occaecat cupidatat</p>
<a class="abs section-link" style="left:112px;top:2763px">View All Products</a>
<div class="abs product" style="left:114px;top:2802px;width:239px;height:334px"><div class="pic" style="height:265px;background:radial-gradient(ellipse 80px 60px at 50% 55%,#e04c7a 0%,#4a6fd0 45%,#f2d04a 70%,rgba(238,240,242,0) 100%),var(--card-bg)" role="img" aria-label="Colourful desk organiser with stationery"></div><p class="name">Office Supplies</p><p class="price">$23.00</p></div>
<div class="abs" style="left:377px;top:2802px;width:239px;height:334px;background:var(--green);padding:148px 0 0 17px">
  <p style="font-size:12px">Today Only</p>
  <p style="font-size:18px;font-weight:600;margin-top:8px">Shop Our Newest Sale</p>
</div>
<div class="abs product" style="left:641px;top:2802px;width:239px;height:334px"><div class="pic" style="height:265px;background:radial-gradient(ellipse 80px 60px at 50% 50%,#c49a64 0%,#d8b98a 50%,rgba(238,240,242,0) 100%),var(--card-bg)" role="img" aria-label="Open box with packing peanuts and scissors"></div><span class="badge">Sale</span><p class="name">Packing Supplies</p><p class="price">$23.00</p></div>
<div class="abs product" style="left:904px;top:2802px;width:239px;height:334px"><div class="pic" style="height:265px;background:radial-gradient(ellipse 80px 80px at 50% 50%,#e0683a 0%,#e8c44a 40%,#7a8a9a 65%,rgba(238,240,242,0) 100%),var(--card-bg)" role="img" aria-label="Shopping cart full of stationery"></div><span class="badge">Sold Out</span><p class="name">Office Supplies</p><p class="price"><span class="now">$23.00</span><span class="old">34.890</span></p></div>
<div class="abs product" style="left:1167px;top:2802px;width:239px;height:334px"><div class="pic" style="height:265px;background:radial-gradient(ellipse 80px 60px at 50% 55%,#3a8ad0 0%,#e8a23a 50%,rgba(238,240,242,0) 100%),var(--card-bg)" role="img" aria-label="Office stationery set"></div><p class="name">Office Supplies</p><p class="price">$23.00</p></div>

<h2 class="abs section-title" style="left:110px;top:3200px">Most popular</h2>
<p class="abs section-sub" style="left:110px;top:3245px">Excepteur sint occaecat cupidatat</p>
<a class="abs section-link" style="left:112px;top:3276px">View All Products</a>
<div class="abs" style="left:115px;top:3341px;width:972px;height:478px;background:radial-gradient(ellipse 160px 200px at 420px 260px,#d9a880 0%,rgba(217,168,128,0) 100%),radial-gradient(ellipse 200px 240px at 650px 240px,#b88060 0%,#cfc7bd 60%,rgba(207,199,189,0) 100%),radial-gradient(ellipse 110px 130px at 200px 380px,#f1f0ec 0%,rgba(241,240,236,0) 100%),linear-gradient(180deg,#bfc3bd 0%,#d3d2cc 60%,#e2dcd2 100%)" role="img" aria-label="Father and son eating breakfast cereal at a kitchen table"></div>

<footer class="abs footer">
  <h2 class="abs">Introduce an email offer</h2>
  <p class="abs lead">Entice shoppers to sign up for your list</p>
  <div class="abs signup"><span class="field">Email</span><span class="send">Subscribe</span></div>
  <div class="abs rule"></div>
  <span class="abs logo">VASTELO</span>
  <div class="abs menu"><a>Home</a><a>About</a><a>Shop</a><a>Blog</a><a>Contact</a></div>
  <p class="abs detail">Additional details about your store</p>
  <p class="abs follow">Follow Us</p>
  <div class="abs social" aria-label="Social links"><span></span><span></span><span></span><span></span></div>
</footer>
<div class="abs copyright">Copyrights@2022.Vastelo.All Rights Reserved</div>

</body>
</html>
```